Cloud Based Internet Protection Service Business Cards

I would like a professionally designed business card. I already have a logo which I have attached.

The business is an online cloud based internet protection service aimed parents, particularly at non-technical parents and also schools.

The card should be be quite simple in its design, not to full of text and give its information in a clear and concise manner

Target Market(s)

Parents (especially non-technical parents) and also schools

Industry/Entity Type

Internet

Colors

Designer to choose colors to be used in the design.

Requirements
Should not have
• Too much text or be too cluttered. No decorative fonts, just a clear and concise font.

```html
<!DOCTYPE html>
<html lang="en">
<head>
<meta charset="UTF-8">
<title>SafeNest Shield – Business Card</title>
<link rel="stylesheet" href="https://fonts.googleapis.com/css2?family=Source+Sans+3:wght@400;600&display=swap">
<style>
  :root {
    --page-bg: #e6e7e9;
    --card-front: #ffffff;
    --card-back: #2c2c2d;
    --brand-deep: #0d5580;
    --brand-light: #4a9fd6;
    --text-blue: #4a9fd6;
    --muted-blue: #2f6f99;
    --rule: #1f5f88;
  }
  * { box-sizing: border-box; margin: 0; padding: 0; }
  html, body {
    width: 1200px; height: 720px; overflow: hidden;
    background: var(--page-bg);
    font-family: "Source Sans 3", "Segoe UI", sans-serif;
  }
  .canvas {
    position: relative; width: 1200px; height: 720px;
    display: flex; align-items: center; justify-content: center; gap: 50px;
  }
  .card {
    position: relative; width: 525px; height: 300px;
    border-radius: 4px;
    box-shadow: 0 12px 30px rgba(0,0,0,.18);
  }
  .card--back { background: var(--card-back); }
  .card--front {
    background: var(--card-front);
    display: flex; align-items: center; justify-content: center;
  }

  .brand { display: flex; align-items: center; gap: 14px; }
  .brand__dot { border-radius: 50%; background: var(--brand-deep); }
  .brand__name {
    font-weight: 600; color: var(--brand-deep);
    letter-spacing: .02em; line-height: 1;
  }
  .card--front .brand__dot { width: 44px; height: 44px; }
  .card--front .brand__name { font-size: 46px; }

  .card--back .brand {
    position: absolute; left: 34px; top: 46px; gap: 10px;
  }
  .card--back .brand__dot { width: 26px; height: 26px; background: var(--brand-light); }
  .card--back .brand__name { font-size: 26px; color: var(--brand-light); }

  .divider {
    position: absolute; left: 270px; top: 40px; width: 1px; height: 200px;
    background: var(--rule);
  }
  .contact {
    position: absolute; left: 292px; top: 52px;
    color: var(--text-blue);
  }
  .contact__name { font-size: 26px; font-weight: 400; line-height: 1.1; }
  .contact__role { font-size: 15px; color: var(--muted-blue); margin-bottom: 22px; }
  .contact__line { font-size: 16px; line-height: 1.65; }
</style>
</head>
<body>
  <main class="canvas">
    <section class="card card--back" aria-label="Card back">
      <div class="brand">
        <span class="brand__dot"></span>
        <span class="brand__name">SafeNest Shield</span>
      </div>
      <div class="divider"></div>
      <div class="contact">
        <p class="contact__name">Daniel Ross</p>
        <p class="contact__role">Manager</p>
        <p class="contact__line">+ 555 - 014 - 2270</p>
        <p class="contact__line">daniel@safenestshield.com</p>
        <p class="contact__line">Safenestshield.com</p>
      </div>
    </section>

    <section class="card card--front" aria-label="Card front">
      <div class="brand">
        <span class="brand__dot"></span>
        <span class="brand__name">SafeNest Shield</span>
      </div>
    </section>
  </main>
</body>
</html>
```